Packaging design for a reclosable bag for our product

We have a logo, and we need to put it on packaging for our product and while we want the look to be simple, we want it to follow good design principles and also contain spaces for other product descriptions.

There will be 5 sizes at launch so I'd like 5 variations, one for each size.

I've included a few mockups of the type of bag that I made but they are all just rough ideas that I had.

I want the brand to look scientific and methodical and even a bit quirky, as in "wow this is a serious product but also a bit unusual."

```html
<!DOCTYPE html>
<html lang="en">
<head>
<meta charset="utf-8">
<title>QV7 Bias Lighting – Pouch Options</title>
<link rel="stylesheet" href="https://fonts.googleapis.com/css2?family=Montserrat:wght@400;800&family=Open+Sans:wght@400;500&family=Great+Vibes&family=Allura&family=Poiret+One&family=Tinos&display=swap">
<style>
  :root {
    --board: #ececec;
    --ink: #151515;
    --pouch-dark: #1e1e1e;
    --pouch-dark-hi: #3a3a3a;
    --pouch-light: #f4f4f4;
    --pouch-light-lo: #dcdcdc;
    --paper: #ffffff;
    --rule-line: #cfcfcf;
  }
  * { margin: 0; padding: 0; box-sizing: border-box; }
  html, body { width: 1200px; height: 2501px; overflow: hidden; }
  body { background: var(--board); position: relative; font-family: "Open Sans", sans-serif; }

  .option-row { position: absolute; left: 0; width: 1200px; height: 833px; border-bottom: 2px solid var(--rule-line); }
  .option-row.row-1 { top: 0; }
  .option-row.row-2 { top: 833px; }
  .option-row.row-3 { top: 1666px; }

  .option-label {
    position: absolute; left: 58px; top: 380px;
    transform: translate(-50%, -50%) rotate(-90deg);
    font-family: "Tinos", serif; font-size: 74px; color: var(--ink); white-space: nowrap; letter-spacing: 1px;
  }

  .pouch { position: absolute; width: 444px; height: 600px; text-align: center; }
  .pouch.left { left: 143px; }
  .pouch.right { left: 638px; }
  .pouch.dark { background: radial-gradient(ellipse at 45% 40%, var(--pouch-dark-hi), var(--pouch-dark) 70%); color: var(--paper); --fg: var(--paper); }
  .pouch.light { background: radial-gradient(ellipse at 50% 40%, var(--paper), var(--pouch-light) 50%, var(--pouch-light-lo)); color: var(--ink); --fg: var(--ink); }
  .pouch .seal { position: absolute; left: 16px; right: 16px; top: 80px; height: 3px; background: currentColor; opacity: .18; }

  .pouch > * { position: absolute; left: 0; right: 0; }
  .brand-name { font-family: "Montserrat", sans-serif; font-weight: 800; letter-spacing: -3px; line-height: 1; }
  .script-line { font-family: "Great Vibes", cursive; line-height: 1; }
  .deco-line { font-family: "Poiret One", sans-serif; line-height: 1; }
  .size-class { font-family: "Open Sans", sans-serif; font-weight: 500; letter-spacing: 1px; }
  .spec-text { font-family: "Open Sans", sans-serif; line-height: 1.45; }
  .rule { height: 3px; background: var(--fg); margin: 0 auto; }

  /* Option 1 */
  .row-1 .pouch { top: 90px; }
  .row-1 .brand-name { top: 148px; font-size: 112px; }
  .row-1 .script-line { top: 268px; font-size: 54px; }
  .row-1 .size-class { top: 345px; font-size: 20px; }
  .row-1 .length-script { top: 392px; font-family: "Allura", cursive; font-size: 112px; line-height: 1; }
  .row-1 .rule { top: 500px; width: 228px; }
  .row-1 .spec-text { top: 515px; font-size: 16px; }

  /* Option 2 */
  .row-2 .pouch { top: 85px; }
  .row-2 .brand-name { top: 175px; font-size: 136px; }
  .row-2 .deco-line { top: 320px; font-size: 44px; letter-spacing: 1px; }
  .row-2 .spec-text { top: 412px; font-size: 20px; line-height: 1.5; }
  .row-2 .length-plain { top: 550px; left: 62px; right: auto; font-family: "Montserrat", sans-serif; font-size: 31px; }
  .row-2 .size-class { top: 555px; left: auto; right: 56px; font-size: 20px; font-weight: 400; }

  /* Option 3 */
  .row-3 .pouch { top: 86px; }
  .row-3 .brand-name { top: 208px; font-size: 112px; }
  .row-3 .script-line { top: 318px; font-size: 50px; }
  .row-3 .size-block { top: 432px; display: flex; justify-content: center; align-items: center; gap: 10px; }
  .row-3 .size-stack { font-family: "Poiret One", sans-serif; text-align: left; line-height: .95; }
  .row-3 .size-stack .small { display: block; font-size: 20px; }
  .row-3 .size-stack .big { display: block; font-size: 38px; }
  .row-3 .divider { width: 3px; height: 74px; background: var(--fg); }
  .row-3 .size-length { font-family: "Poiret One", sans-serif; font-size: 80px; line-height: 1; letter-spacing: 4px; }
  .row-3 .rule { top: 534px; width: 228px; }
  .row-3 .spec-text { top: 545px; font-size: 17px; }
</style>
</head>
<body>

<section class="option-row row-1">
  <div class="option-label">OPTION-1</div>
  <div class="pouch dark left">
    <div class="seal"></div>
    <div class="brand-name">QV7</div>
    <div class="script-line">Bias Lighting</div>
    <div class="size-class">EXTRA LARGE</div>
    <div class="length-script">5m</div>
    <div class="rule"></div>
    <p class="spec-text">6500K White Bias Lighting<br>Simulated D65 CRI 90+</p>
  </div>
  <div class="pouch light right">
    <div class="seal"></div>
    <div class="brand-name">QV7</div>
    <div class="script-line">Bias Lighting</div>
    <div class="size-class">EXTRA LARGE</div>
    <div class="length-script">5m</div>
    <div class="rule"></div>
    <p class="spec-text">6500K White Bias Lighting<br>Simulated D65 CRI 90+</p>
  </div>
</section>

<section class="option-row row-2">
  <div class="option-label">OPTION-2</div>
  <div class="pouch dark left">
    <div class="seal"></div>
    <div class="brand-name">QV7</div>
    <div class="deco-line">BIAS&nbsp;&nbsp;LIGHTING</div>
    <p class="spec-text">6500K White Bias Lighting<br>Simulated D65 CRI 90+</p>
    <div class="length-plain">5m</div>
    <div class="size-class">EXTRA LARGE</div>
  </div>
  <div class="pouch light right">
    <div class="seal"></div>
    <div class="brand-name">QV7</div>
    <div class="deco-line">BIAS&nbsp;&nbsp;LIGHTING</div>
    <p class="spec-text">6500K White Bias Lighting<br>Simulated D65 CRI 90+</p>
    <div class="length-plain">5m</div>
    <div class="size-class">EXTRA LARGE</div>
  </div>
</section>

<section class="option-row row-3">
  <div class="option-label">OPTION-3</div>
  <div class="pouch dark left">
    <div class="seal"></div>
    <div class="brand-name">QV7</div>
    <div class="script-line">Bias Lighting</div>
    <div class="size-block">
      <div class="size-stack"><span class="small">EXTRA</span><span class="big">LARGE</span></div>
      <div class="divider"></div>
      <div class="size-length">5 M</div>
    </div>
    <div class="rule"></div>
    <p class="spec-text">6500k White Bias Lighting<br>Simulated D65 Cri 90+</p>
  </div>
  <div class="pouch light right">
    <div class="seal"></div>
    <div class="brand-name">QV7</div>
    <div class="script-line">Bias Lighting</div>
    <div class="size-block">
      <div class="size-stack"><span class="small">EXTRA</span><span class="big">LARGE</span></div>
      <div class="divider"></div>
      <div class="size-length">5 M</div>
    </div>
    <div class="rule"></div>
    <p class="spec-text">6500k White Bias Lighting<br>Simulated D65 Cri 90+</p>
  </div>
</section>

</body>
</html>
```